Social Media Cover and Profile

We already have our own logo. We just need a fresh design on our social media pages. We are not happy with our current designs. We would like to incorporate our YIKE billboard and the colors are blue (#05143f) and white. You can also incorporate silver as well. We are a family law office (Divorce and Custody) We no longer want to incorporate the Spire of Dunvale photo that we are currently using. You can look at our Friendbook page; The Law Office of Miles T. Hadley.

Target Market(s)

Potential Clients

Industry/Entity Type

Family Law

Logo Text

Our Logo Is The Law Office of Miles T. Hadley with the Sheild

Requirements
Must have
• Text to include:
Central Pennslyvania's Premier Family Law Firm

Ability to be resized to and used as all images in social media, including but not limited to: Youtube Channel art, Friendbook Cover and Profile.
Nice to have
• Darker color but we are open to "bright" ideas.

```html
<!DOCTYPE html>
<html lang="en">
<head>
<meta charset="utf-8">
<title>Miles T. Hadley – Social Cover Concepts</title>
<link rel="stylesheet" href="https://fonts.googleapis.com/css2?family=Cinzel:wght@400;600&family=Montserrat:wght@700;800&family=Roboto:wght@400;500;700&display=swap">
<style>
:root{
  --sheet:#1f1f1f;
  --navy:#05143f;
  --navy-deep:#030b2a;
  --white:#ffffff;
  --silver-hi:#f4f4f4;
  --silver-mid:#bdbdbd;
  --silver-lo:#8e8e8e;
  --ui-bg:#ffffff;
  --ui-pill:#f0f2f5;
  --ui-text:#65676b;
  --ui-dark:#050505;
  --ui-blue:#1877f2;
  --ui-red:#e41e3f;
  --label:#e6e6e6;
  --dim:#4a4a4a;
}
*{margin:0;padding:0;box-sizing:border-box}
html,body{width:833px;height:1200px;overflow:hidden;background:var(--sheet)}
body{position:relative;font-family:"Roboto",sans-serif}
.abs{position:absolute}

/* header */
.brand-head{left:55px;top:62px;display:flex;align-items:center;gap:10px}
.brand-mark{width:40px;height:46px;border:2px solid var(--white)}
.brand-name{font-family:"Cinzel",serif;font-weight:400;color:var(--white);font-size:17px;line-height:1.05;letter-spacing:.3px}
.brand-name small{display:block;font-size:9px}
.size-tag{font-family:"Roboto",sans-serif;color:var(--dim);font-size:27px;letter-spacing:.5px}
.size-tag.top{right:35px;top:90px}
.size-tag.vertical{left:425px;top:1036px;transform:translate(-50%,-50%) rotate(-90deg);white-space:nowrap;font-size:26px}

/* page mockup */
.page{width:747px;height:332px;left:52px;background:var(--ui-bg);overflow:hidden}
.topbar{height:31px;position:relative;background:var(--ui-bg)}
.site-dot{left:8px;top:5px;width:22px;height:22px;border-radius:50%;background:var(--ui-blue)}
.search{left:36px;top:5px;width:153px;height:22px;border-radius:11px;background:var(--ui-pill);font-size:8.5px;color:var(--ui-text);padding:6px 0 0 20px}
.search::before{content:"";position:absolute;left:7px;top:6px;width:7px;height:7px;border:1.3px solid var(--ui-text);border-radius:50%}
.nav-icon{top:9px;width:13px;height:13px;border:1.5px solid var(--ui-text);border-radius:3px}
.round-btn{top:6px;width:20px;height:20px;border-radius:50%;background:#e4e6eb}
.badge{width:9px;height:9px;border-radius:50%;background:var(--ui-red);color:#fff;font-size:6px;text-align:center;line-height:9px}
.side-l{left:0;top:33px;width:111px;height:160px;background:linear-gradient(180deg,#7f90b4 0%,#b9c4d8 55%,#fff 100%)}
.side-r{right:9px;top:33px;width:111px;height:160px;background:linear-gradient(180deg,#8a7a63 0%,#c8bfb2 55%,#fff 100%)}
.scrollbar{right:0;top:0;width:9px;height:100%;background:#f1f1f1}
.scrollbar::after{content:"";position:absolute;left:2px;top:10px;width:5px;height:50px;background:#c2c2c2;border-radius:2px}

.profile-pic{left:130px;top:217px;width:74px;height:74px;border-radius:50%;background:#fff;border:1px solid #dadde1;display:flex;align-items:center;justify-content:center}
.profile-pic span{background:#000;color:#fff;font-family:"Cinzel",serif;font-size:5px;padding:5px 4px;width:56px;text-align:center}
.page-name{left:218px;top:236px;font-weight:700;font-size:15px;line-height:18px;color:var(--ui-dark);width:210px}
.page-cat{left:218px;top:275px;font-size:9.5px;color:var(--ui-text)}
.call-btn{left:438px;top:264px;width:170px;height:22px;background:var(--ui-blue);border-radius:4px;color:#fff;font-size:9.5px;font-weight:500;display:flex;align-items:center;justify-content:center;gap:4px}
.rule{left:129px;top:301px;width:479px;height:1px;background:#dadde1}
.tabs{left:138px;top:312px;display:flex;gap:17px;font-size:8.5px;color:var(--ui-text)}
.tabs .on{color:var(--ui-blue)}
.actions{left:427px;top:308px;display:flex;gap:5px}
.actions span{background:#e4e6eb;height:20px;border-radius:4px;font-size:8.5px;color:var(--ui-dark);display:flex;align-items:center;justify-content:center}

/* cover art */
.cover{position:absolute;overflow:hidden;background:linear-gradient(120deg,var(--navy-deep) 0%,var(--navy) 45%,#0a1d55 100%)}
.cover::after{content:"";position:absolute;right:-10px;top:8%;width:32%;height:90%;border:2px solid rgba(255,255,255,.04);border-radius:0 0 50% 50%}
.silver{background:linear-gradient(100deg,var(--silver-lo) 0%,var(--silver-hi) 30%,var(--silver-mid) 55%,var(--silver-hi) 80%,var(--silver-lo) 100%)}
.billboard-word{position:absolute;font-family:"Cinzel",serif;font-weight:600;line-height:1;background:linear-gradient(180deg,#ffffff 0%,#cfcfcf 45%,#8d8d8d 60%,#f2f2f2 100%);-webkit-background-clip:text;background-clip:text;color:transparent;letter-spacing:2px}
.tagline-serif{position:absolute;font-family:"Cinzel",serif;font-weight:400;color:var(--white);line-height:1}
.tagline-sans{position:absolute;font-family:"Montserrat",sans-serif;font-weight:800;color:var(--white);text-align:center;line-height:1.1;left:0;width:100%}
.divider{position:absolute;width:1px;background:rgba(255,255,255,.45)}
.url{position:absolute;font-family:"Roboto",sans-serif;color:var(--navy-deep);white-space:nowrap}
.lockup{position:absolute;display:flex;align-items:center;gap:5px}
.lockup i{display:block;border:1.5px solid var(--navy)}
.lockup b{font-family:"Cinzel",serif;font-weight:400;color:var(--navy);line-height:1}
.lockup b small{display:block}

.sample-label{left:57px;font-size:13px;letter-spacing:5px;color:var(--label)}
.caption{font-size:8px;color:var(--label)}
</style>
</head>
<body>

<div class="abs brand-head">
  <div class="brand-mark"></div>
  <div class="brand-name"><small>The Law Office of</small>Miles T. Hadley</div>
</div>
<div class="abs size-tag top">851X310</div>

<!-- Sample 1 page -->
<section class="abs page" style="top:141px">
  <div class="topbar">
    <div class="abs site-dot"></div>
    <div class="abs search">Search Friendbook</div>
    <div class="abs nav-icon" style="left:231px"></div>
    <div class="abs nav-icon" style="left:296px"></div><div class="abs badge" style="left:306px;top:5px">9</div>
    <div class="abs nav-icon" style="left:362px"></div>
    <div class="abs nav-icon" style="left:427px;border-radius:50%"></div>
    <div class="abs nav-icon" style="left:493px"></div>
    <div class="abs round-btn" style="left:629px"></div>
    <div class="abs round-btn" style="left:655px"></div>
    <div class="abs round-btn" style="left:681px"></div><div class="abs badge" style="left:694px;top:3px">5</div>
    <div class="abs round-btn" style="left:707px"></div>
  </div>
  <div class="abs side-l"></div><div class="abs side-r"></div>

  <div class="cover" style="left:111px;top:33px;width:516px;height:192px">
    <div class="abs silver" style="left:0;top:0;width:215px;height:48px;clip-path:polygon(0 0,100% 0,80% 100%,0 100%)"></div>
    <div class="lockup" style="left:19px;top:8px"><i style="width:26px;height:30px"></i><b style="font-size:11px"><small style="font-size:5px">The Law Office of</small>Miles T. Hadley</b></div>
    <div class="billboard-word" style="left:24px;top:70px;font-size:66px">YIKE</div>
    <div class="divider" style="left:257px;top:40px;height:102px"></div>
    <div class="tagline-serif" style="left:281px;top:38px;font-size:24px;line-height:26px">Central<br>Pennslyvania's<br>Premier Family<br>Law Firm</div>
    <div class="abs silver" style="left:0;top:163px;width:100%;height:29px"></div>
    <div class="url" style="left:0;width:100%;text-align:center;top:171px;font-size:11px;letter-spacing:8px">www.mileshadleylaw.com</div>
  </div>

  <div class="abs profile-pic"><span>Miles T. Hadley</span></div>
  <div class="abs page-name">The Law Office of Miles T. Hadley</div>
  <div class="abs page-cat">Divorce &amp; Family Lawyer</div>
  <div class="abs call-btn"><svg width="9" height="9" viewBox="0 0 24 24"><path fill="#fff" d="M6.6 10.8a15 15 0 0 0 6.6 6.6l2.2-2.2c.3-.3.7-.4 1-.2 1.1.4 2.3.6 3.6.6.6 0 1 .4 1 1V20c0 .6-.4 1-1 1A17 17 0 0 1 3 4c0-.6.4-1 1-1h3.5c.6 0 1 .4 1 1 0 1.3.2 2.5.6 3.6.1.3 0 .7-.2 1z"/></svg>Call Now</div>
  <div class="abs rule"></div>
  <div class="abs tabs"><span class="on">Home</span><span>Photos</span><span>Videos</span><span>About</span><span>More ▾</span></div>
  <div class="abs actions"><span style="width:59px">Like</span><span style="width:58px">Message</span><span style="width:26px">⌕</span><span style="width:24px">···</span></div>
  <div class="abs scrollbar"></div>
</section>
<div class="abs sample-label" style="top:484px">SAMPLE 1</div>

<!-- Sample 2 page -->
<section class="abs page" style="top:522px">
  <div class="topbar">
    <div class="abs site-dot"></div>
    <div class="abs search">Search Friendbook</div>
    <div class="abs nav-icon" style="left:231px"></div>
    <div class="abs nav-icon" style="left:296px"></div><div class="abs badge" style="left:306px;top:5px">9</div>
    <div class="abs nav-icon" style="left:362px"></div>
    <div class="abs nav-icon" style="left:427px;border-radius:50%"></div>
    <div class="abs nav-icon" style="left:493px"></div>
    <div class="abs round-btn" style="left:629px"></div>
    <div class="abs round-btn" style="left:655px"></div>
    <div class="abs round-btn" style="left:681px"></div><div class="abs badge" style="left:694px;top:3px">5</div>
    <div class="abs round-btn" style="left:707px"></div>
  </div>
  <div class="abs side-l"></div><div class="abs side-r"></div>

  <div class="cover" style="left:111px;top:31px;width:516px;height:193px">
    <div class="billboard-word" style="left:0;width:100%;text-align:center;top:18px;font-size:56px">YIKE</div>
    <div class="tagline-sans" style="top:87px;font-size:21px">CENTRAL PENNSLYVANIA'S PREMIER<br>FAMILY LAW FIRM</div>
    <div class="abs" style="left:0;top:145px;width:100%;height:48px;background:var(--white)"></div>
    <div class="abs silver" style="left:203px;top:145px;width:313px;height:48px;clip-path:polygon(14% 0,100% 0,100% 100%,0 100%)"></div>
    <div class="lockup" style="left:19px;top:152px"><i style="width:26px;height:32px"></i><b style="font-size:11px"><small style="font-size:5px">The Law Office of</small>Miles T. Hadley</b></div>
    <div class="url" style="right:18px;top:163px;font-size:12px;letter-spacing:2.5px">WWW.MILESHADLEYLAW.COM</div>
  </div>

  <div class="abs profile-pic"><span>Miles T. Hadley</span></div>
  <div class="abs page-name">The Law Office of Miles T. Hadley</div>
  <div class="abs page-cat">Divorce &amp; Family Lawyer</div>
  <div class="abs call-btn"><svg width="9" height="9" viewBox="0 0 24 24"><path fill="#fff" d="M6.6 10.8a15 15 0 0 0 6.6 6.6l2.2-2.2c.3-.3.7-.4 1-.2 1.1.4 2.3.6 3.6.6.6 0 1 .4 1 1V20c0 .6-.4 1-1 1A17 17 0 0 1 3 4c0-.6.4-1 1-1h3.5c.6 0 1 .4 1 1 0 1.3.2 2.5.6 3.6.1.3 0 .7-.2 1z"/></svg>Call Now</div>
  <div class="abs rule"></div>
  <div class="abs tabs"><span class="on">Home</span><span>Photos</span><span>Videos</span><span>About</span><span>More ▾</span></div>
  <div class="abs actions"><span style="width:59px">Like</span><span style="width:58px">Message</span><span style="width:26px">⌕</span><span style="width:24px">···</span></div>
  <div class="abs scrollbar"></div>
</section>
<div class="abs sample-label" style="top:871px">SAMPLE 2</div>

<!-- Group cover 1 -->
<div class="cover" style="left:52px;top:937px;width:336px;height:176px">
  <div class="billboard-word" style="left:14px;top:40px;font-size:44px">YIKE</div>
  <div class="divider" style="left:166px;top:24px;height:64px"></div>
  <div class="tagline-serif" style="left:182px;top:23px;font-size:16.5px;line-height:17px">Central<br>Pennslyvania's<br>Premier Family<br>Law Firm</div>
  <div class="abs silver" style="left:42px;top:104px;width:252px;height:51px;clip-path:polygon(12% 0,88% 0,100% 100%,0 100%)"></div>
  <div class="lockup" style="left:89px;top:112px"><i style="width:28px;height:34px"></i><b style="font-size:12px"><small style="font-size:5.5px">The Law Office of</small>Miles T. Hadley</b></div>
  <div class="abs silver" style="left:0;top:155px;width:100%;height:21px"></div>
  <div class="url" style="left:0;width:100%;text-align:center;top:159px;font-size:8px;letter-spacing:5.5px">www.mileshadleylaw.com</div>
</div>

<div class="abs size-tag vertical">820X428</div>

<!-- Group cover 2 -->
<div class="cover" style="left:460px;top:937px;width:337px;height:176px">
  <div class="billboard-word" style="left:0;width:100%;text-align:center;top:24px;font-size:50px">YIKE</div>
  <div class="tagline-sans" style="top:89px;font-size:18.5px;line-height:20px">CENTRAL PENNSLYVANIA'S<br>PREMIER FAMILY LAW FIRM</div>
  <div class="abs" style="left:0;top:142px;width:100%;height:34px;background:var(--white)"></div>
  <div class="abs silver" style="left:128px;top:142px;width:209px;height:34px;clip-path:polygon(12% 0,100% 0,100% 100%,0 100%)"></div>
  <div class="lockup" style="left:13px;top:147px"><i style="width:17px;height:22px"></i><b style="font-size:7.5px"><small style="font-size:3.5px">The Law Office of</small>Miles T. Hadley</b></div>
  <div class="url" style="right:12px;top:155px;font-size:8px;letter-spacing:1.5px">WWW.MILESHADLEYLAW.COM</div>
</div>

<div class="abs caption" style="left:51px;top:1127px">GROUP COVER PHOTO_SAMPLE 1</div>
<div class="abs caption" style="left:460px;top:1127px">GROUP COVER PHOTO_SAMPLE 2</div>

</body>
</html>
```